New Template design for Website in Wordpress

We are interested in changing our website look at www.cargolinx.com -We also are very interested in Have it done in Wordpress in which we are understanding the search engines are liking a bit more. The website we would want to try working with on this is www.cargolinx.com. We look forward to seeing the different design ideas please just make sure they are in wordpress! Thanks, Marlen

Reason: need more design idea..... We would still like to use our pictures off our site since we paid for them so keep that in mind as well as we would still want the rotating pictures in the head of the page but not in Flash.

```html
<!DOCTYPE html>
<html lang="en">
<head>
<meta charset="utf-8">
<title>CargoLinx – A Diversified Freight Company</title>
<link href="https://fonts.googleapis.com/css2?family=Ubuntu:wght@300;400;500;700&display=swap" rel="stylesheet">
<style>
:root{
  --red:#a50f0b;
  --dark:#3d3d3d;
  --text:#5a5a5a;
  --muted:#8a8a8a;
  --line:#dcdcdc;
  --bg:#f6f6f6;
  --white:#ffffff;
  --footer:#262626;
}
*{box-sizing:border-box;margin:0;padding:0}
html,body{width:1081px;height:1200px;overflow:hidden}
body{background:var(--bg);font-family:"Ubuntu",sans-serif;font-weight:300;color:var(--text);position:relative;border-top:3px solid #c4c4c4}
.wrap{position:absolute;left:99px;width:882px}
a{color:inherit;text-decoration:none}

/* header */
.site-header{position:absolute;top:0;left:0;width:1081px;height:108px;background:#fbfbfb}
.brand{top:30px}
.brand-name{font-weight:700;font-size:29px;color:var(--red);letter-spacing:1px;line-height:32px}
.brand-tag{font-size:16px;font-weight:300;color:#777;margin-top:1px}
.social{position:absolute;left:848px;top:0;display:flex;gap:9px}
.social span{width:26px;height:34px;background:#2f8ac9;border-radius:0 0 4px 4px;display:block}
.social span:nth-child(2){background:#3b5ba6}
.social span:nth-child(3){background:#d0402e}
.call{position:absolute;right:100px;top:52px;text-align:right}
.call p{font-size:15px;font-weight:400;color:#555}
.call strong{display:block;font-size:22px;font-weight:500;color:var(--red);margin-top:2px}

/* nav */
.main-nav{position:absolute;top:108px;left:0;width:1081px;height:38px;background:#efefef;border-top:1px solid #e3e3e3;border-bottom:1px solid #e3e3e3}
.main-nav ul{list-style:none;display:flex;gap:26px;position:absolute;left:99px;top:11px;font-size:13px;font-weight:500;color:#333}
.main-nav li.active{color:var(--red);position:relative}
.main-nav li.active::after{content:"";position:absolute;left:14px;top:17px;border:5px solid transparent;border-bottom-color:var(--red)}
.search{position:absolute;left:780px;top:3px;width:201px;height:30px;background:#c9c9c9;display:flex;align-items:center;padding:0 10px;font-style:italic;font-size:12px;font-weight:400;color:#666;justify-content:space-between}

/* slider */
.hero{top:156px;height:346px;background:#efefef;border:1px solid #e2e2e2;overflow:hidden}
.hero-photo{position:absolute;left:245px;top:0;width:637px;height:346px;background:linear-gradient(180deg,#e4eaef 0%,#c9d3dc 55%,#6d97ad 100%);-webkit-mask:linear-gradient(90deg,transparent,#000 35%);mask:linear-gradient(90deg,transparent,#000 35%)}
.hero-copy{position:absolute;left:17px;top:104px}
.hero-copy h1{font-size:26px;font-weight:500;color:var(--dark);line-height:30px}
.hero-copy h2{font-size:28px;font-weight:400;color:var(--red);line-height:32px}
.hero-copy p{font-size:15px;font-weight:300;color:#666;margin-top:12px}
.btn{display:inline-block;background:var(--red);color:#fff;font-weight:300;border-radius:2px}
.hero-copy .btn{margin-top:16px;font-size:15px;padding:9px 8px}
.dots{display:flex;gap:3px}
.dots i{width:7px;height:7px;background:#c8c8c8;display:block}
.dots i:first-child{background:var(--red)}
.hero .dots{position:absolute;left:17px;top:317px}

.divider{position:absolute;top:513px;left:0;width:1081px;border-top:2px solid #e6e6e6}

/* services */
.services-head{top:533px}
.section-title{font-size:21px;font-weight:500;color:var(--red)}
.services-head .dots{position:absolute;right:0;top:11px}
.services-head p{font-size:15px;color:#888;margin-top:8px}
.cards{top:610px;display:flex;gap:7px}
.card{width:215px;height:263px;background:#fff;border:1px solid #e1e1e1;padding:5px;position:relative}
.card-photo{height:145px;display:block}
.card h3{font-weight:400;font-size:14px;color:#555;padding:8px 0 7px;border-bottom:1px solid #e2e2e2;margin:0 -2px}
.card p{font-size:11px;line-height:16px;color:#8a8a8a;margin-top:7px}
.card .more{position:absolute;right:5px;bottom:6px;font-style:italic;font-weight:400;font-size:11.5px;color:var(--red)}

/* bottom */
.about{top:897px;width:560px}
.about h2,.links h2{font-weight:500;font-size:17px}
.about h2{color:#444}
.about p{font-size:11.5px;line-height:18px;color:#8a8a8a;margin-top:13px}
.about p+p{margin-top:18px}
.about .btn{margin-top:11px;font-size:15px;padding:8px 14px}
.vline{position:absolute;left:670px;top:897px;height:232px;border-left:1px solid #e0e0e0}
.links{left:690px;top:897px;width:291px}
.links h2{color:var(--red)}
.links .arrows{position:absolute;right:0;top:3px;color:#aaa;font-size:12px;letter-spacing:8px}
.links ul{list-style:none;margin-top:13px;font-size:11.5px;line-height:18px;color:#8a8a8a}
.like{display:flex;align-items:center;gap:5px;margin-top:9px;font-size:9px;font-weight:400;color:#333;white-space:nowrap}
.like b{background:#4267b2;color:#fff;font-weight:500;padding:2px 6px 2px 4px;font-size:10px;display:flex;align-items:center;gap:3px}
.like b::before{content:"";width:8px;height:8px;background:#fff;display:block}
.quote{display:flex;justify-content:space-between;align-items:center;width:171px;height:45px;background:#1e1e1e;color:#fff;padding:0 8px 0 13px;margin-top:9px;white-space:nowrap}
.quote strong{display:block;font-size:14.5px;font-weight:500;line-height:17px}
.quote small{display:block;font-size:11px;font-weight:400;line-height:14px}
.quote span{font-size:20px;color:#aaa}

.site-footer{position:absolute;left:0;top:1161px;width:1081px;height:39px;background:var(--footer);color:#fff;font-size:11.5px;font-weight:400}
.site-footer .wrap{top:12px;display:flex;justify-content:space-between}
</style>
</head>
<body>
<header class="site-header">
  <div class="wrap brand">
    <div class="brand-name">CARGOLINX</div>
    <div class="brand-tag">A DIVERSIFIED FREIGHT COMPANY</div>
  </div>
  <div class="social" aria-label="Social links"><span></span><span></span><span></span><span></span></div>
  <div class="call"><p>Call Us Today!</p><strong>(555)014-2290</strong></div>
</header>

<nav class="main-nav">
  <ul>
    <li class="active">HOME</li>
    <li>INSURANCE &amp; LEGAL INFO</li>
    <li>FAST FREIGHT QUOTE</li>
  </ul>
  <div class="search">Search here...
    <svg width="18" height="18" viewBox="0 0 18 18"><circle cx="7" cy="7" r="5.5" fill="none" stroke="#555" stroke-width="2.2"/><line x1="11" y1="11" x2="16.5" y2="16.5" stroke="#555" stroke-width="2.8" stroke-linecap="round"/></svg>
  </div>
</nav>

<section class="wrap hero">
  <div class="hero-photo" role="img" aria-label="Container cargo ship sailing on the sea"></div>
  <div class="hero-copy">
    <h1>WELCOME TO CARGOLINX</h1>
    <h2>A Diversified Freight Company</h2>
    <p>Lorem ipsum dolor sit amet consectetur adipsicing elit.</p>
    <a class="btn" href="#">Click Here For FREIGHT QUOTE</a>
  </div>
  <div class="dots"><i></i><i></i><i></i><i></i><i></i></div>
</section>

<div class="divider"></div>

<section class="wrap services-head">
  <h2 class="section-title">Our Services</h2>
  <div class="dots"><i></i><i></i><i></i><i></i></div>
  <p>Lorem ipsum dolor sit amet, consectetur adipisicing elit, sed do eiusmod tempor incididunt ut labore et dolore magna aliqua.</p>
</section>

<div class="wrap cards">
  <article class="card">
    <div class="card-photo" role="img" aria-label="Oversize load truck on a highway" style="background:linear-gradient(160deg,#7a9a6a,#b89a4a)"></div>
    <h3>Heavy Haul Services</h3>
    <p>Lorem ipsum dolor sit amet consectetu-adipiscing elit, Sed do euismod tempor incidunt magna aliqua..</p>
    <a class="more" href="#">Read More..</a>
  </article>
  <article class="card">
    <div class="card-photo" role="img" aria-label="Red semi truck with refrigerated trailer" style="background:linear-gradient(160deg,#d8dde2,#a9a4a6)"></div>
    <h3>Dry &amp; Refrigerated Services</h3>
    <p>Lorem ipsum dolor sit amet consectetu-adipiscing elit, Sed do euismod tempor incidunt magna aliqua..</p>
    <a class="more" href="#">Read More..</a>
  </article>
  <article class="card">
    <div class="card-photo" role="img" aria-label="Flatbed truck driving on a road" style="background:linear-gradient(160deg,#5e615e,#9a9d98)"></div>
    <h3>Flatbed &amp; Piggy Back Services</h3>
    <p>Lorem ipsum dolor sit amet consectetu-adipiscing elit, Sed do euismod tempor incidunt magna aliqua..</p>
    <a class="more" href="#">Read More..</a>
  </article>
  <article class="card">
    <div class="card-photo" role="img" aria-label="Container ship at sea" style="background:linear-gradient(160deg,#b9c4ce,#2c3b55)"></div>
    <h3>Freight Ocean Services</h3>
    <p>Lorem ipsum dolor sit amet consectetu-adipiscing elit, Sed do euismod tempor incidunt magna aliqua..</p>
    <a class="more" href="#">Read More..</a>
  </article>
</div>

<section class="wrap about">
  <h2>WORLDWIDE SHIPPING- OCEAN AND TRUCKING WITH NO LIMITS</h2>
  <p>Welcome to CargoLinx and Linx Freight Inc. We are a one stop solution logistics company servicing Worldwide with our Trucking and Ocean shipping service. In using our freight services, we will negotiate a competitive freight quote using over 5000 different carriers who are certified and contracted by us. We have all equipment types available daily, service all freight types, and have no limits Worldwide.</p>
  <p>Whether you need a freight quote for a full load, LTL/Partial load, or Oversized Machinery or Equipment, trucking and/or ocean shipment, we will take care of it. All your freight or equipment to be shipped will be covered in full by our insurance with no limitations to match its value.</p>
  <a class="btn" href="#">Learn More</a>
</section>

<div class="vline"></div>

<aside class="wrap links">
  <h2>WORLDWIDE FREIGHT SERVICES</h2>
  <span class="arrows">‹›</span>
  <ul>
    <li>Worldwide Shipping Scope</li>
    <li>Trucking Shipping Services</li>
    <li>Ocean Shipping Services</li>
    <li>Insurance &amp; Legal Details</li>
    <li>Get a Freight Quote Now!</li>
    <li>Return to Home Page</li>
  </ul>
  <div class="like"><b>Like</b>61,725 people like this. Be the first of your friends.</div>
  <a class="quote" href="#"><div><strong>GET A FREE QUOTE</strong><small>IN 2 MINUTES OR LESS</small></div><span>❯</span></a>
</aside>

<footer class="site-footer">
  <div class="wrap">
    <span>Copyrights © 2014 CargoLinx.com -- Equipment Transport Specialist</span>
    <span>All Rights Reserved &nbsp; | &nbsp; Privacy Policy</span>
  </div>
</footer>
</body>
</html>
```